CraneHollow - Business Card and Letterhead

After having received some fantastic submissions in our recent logo design project, I would now like to extend our branding to letterheads and business cards.
CraneHollow is a consulting service in the Construction Industry. We deal with both residential and commercial projects, and our clients include Architects, Builders, Tradespeople and Home Owners.
The designs should be simple and effective, convey personal service and professionalism, and display some level of creativity.
For both the business cards and letterhead, a white card stock will be used. This project is for business cards and letterheads only. Our new logo is attached for use.
The designs should incorporate our two main colours which are Blue (RGB 14,92,143) and Green (RGB 132,194,37).
For the time being, please submit all designs showing generic information including name, mobile number, email, postal address and website details. No fax number or physical address is required. I will provide our actual contact details once a final design has been selected.
I encourage you to interpret this brief in your own creative way, and look forward to some quality submissions.
Thanks!
Leo
CraneHollow.

```html
<!DOCTYPE html>
<html lang="en">
<head>
<meta charset="UTF-8">
<title>CraneHollow – Business Card</title>
<link href="https://fonts.googleapis.com/css2?family=Arimo:wght@400;700&display=swap" rel="stylesheet">
<style>
  :root {
    --brand-blue: #0e5c8f;
    --brand-green: #84c225;
    --ink-dark: #5a5b5d;
    --ink-mid: #6f7072;
    --ink-soft: #7d7e80;
    --panel-grey: #e4e5e1;
    --panel-light: #efefec;
    --paper: #ffffff;
  }
  * { margin: 0; padding: 0; box-sizing: border-box; }
  html, body {
    width: 1200px;
    height: 801px;
    overflow: hidden;
    background: var(--paper);
  }
  .card {
    position: relative;
    width: 1200px;
    height: 801px;
    background: var(--paper);
    font-family: "Arimo", Arial, sans-serif;
    overflow: hidden;
  }
  .card-backdrop {
    position: absolute;
    inset: 0;
    width: 1200px;
    height: 801px;
  }
  .brand {
    position: absolute;
    left: 212px;
    top: 14px;
    display: flex;
    align-items: center;
    gap: 18px;
  }
  .brand-square {
    width: 62px;
    height: 62px;
    background: var(--brand-green);
  }
  .brand-name {
    font-size: 76px;
    font-weight: 700;
    color: var(--brand-blue);
    letter-spacing: -1px;
    line-height: 1;
  }
  .holder {
    position: absolute;
    left: 280px;
    top: 305px;
  }
  .holder-name {
    font-size: 42px;
    font-weight: 700;
    color: var(--ink-dark);
    line-height: 1.05;
  }
  .holder-role {
    font-size: 41px;
    font-weight: 400;
    color: var(--ink-mid);
    line-height: 1.1;
  }
  .postal {
    position: absolute;
    left: 30px;
    top: 696px;
    font-size: 15px;
    line-height: 1.3;
    color: var(--ink-soft);
  }
  .contact {
    position: absolute;
    right: 26px;
    top: 696px;
    text-align: right;
    font-size: 14px;
    line-height: 1.3;
    color: var(--ink-soft);
    list-style: none;
  }
</style>
</head>
<body>
<main class="card">
  <svg class="card-backdrop" viewBox="0 0 1200 801" aria-hidden="true">
    <!-- top edge band -->
    <rect x="0" y="0" width="1200" height="10" fill="var(--panel-light)"/>
    <!-- corner panel -->
    <rect x="0" y="0" width="250" height="98" fill="var(--panel-grey)"/>
    <line x1="175" y1="0" x2="175" y2="98" stroke="#fff" stroke-width="3"/>
    <line x1="0" y1="98" x2="250" y2="98" stroke="#fff" stroke-width="3"/>
    <line x1="0" y1="60" x2="175" y2="60" stroke="#fff" stroke-width="2"/>
    <!-- faint brand discs -->
    <circle cx="560" cy="420" r="180" fill="none" stroke="#eef2e8" stroke-width="22"/>
    <circle cx="1080" cy="700" r="120" fill="var(--panel-grey)" opacity="0.7"/>
    <!-- bottom sweep -->
    <path d="M0,600 C260,720 700,760 1200,520 L1200,801 L0,801 Z" fill="var(--panel-light)"/>
    <path d="M0,640 C300,760 760,780 1200,600 L1200,801 L0,801 Z" fill="var(--panel-grey)" opacity="0.6"/>
    <path d="M0,622 C280,740 730,772 1200,560" fill="none" stroke="#fff" stroke-width="4"/>
    <path d="M0,672 C320,778 800,790 1200,650" fill="none" stroke="#fff" stroke-width="2"/>
  </svg>

  <header class="brand">
    <span class="brand-square"></span>
    <span class="brand-name">CraneHollow</span>
  </header>

  <section class="holder">
    <h1 class="holder-name">NAME</h1>
    <p class="holder-role">Managing Director</p>
  </section>

  <address class="postal">
    Address: Dummy address dummy<br>
    00/00 dummy address, dummy.
  </address>

  <ul class="contact">
    <li>Ph: 00 00000000</li>
    <li>email: sdddddddd@mailbox.com</li>
    <li>web: www.dddddddddd.com</li>
  </ul>
</main>
</body>
</html>
```